Cleaning Service Company In need of Good Web presence.

The company is a cleaning service company which provides professional staff and service for cleaning. This is a project to build a site that is both solid and a strong recognition of our organization. It is supposed to show quality, cleanliness, professionalism. The use of images and art for imagery is all good just to have a site that is consistent and solid. There might be a chance to make stationary, logo and business cars if someone feels they can build a brand that is consistent. The image we are going for is clean solid and to stand out. Finally stationary should not be expensive to print.

Current logo is attached and can be used or can be made more creative.

Target Market(s)

Corporate and Government entities, that will feel that this company has a brand that sets it apart from the rest. The company is new so the modification of the logo will not be an issue if a more solid brand come out of this project. The idea is to have a clean consistent product that stands our from others in terms of website, stationary, etc

Industry/Entity Type

Cleaning Service

Contact Information for Business Card

P.O.Box 51947
Riffa
Kingdom of Bahrain

Logo Text

Brightmoor Facility Care

Number of Pages Required

4 page

Font styles to use
Sans Serif

Colors
abd036
cadf82
eaf2ce
9bcb3b

Requirements
Must have
• Green Color to be used in order to stick to the name. Also the creativity and boldness in an elegant manner.
Nice to have
• Arabic name of company
• برايتمور فاسيليتي كير ذ.م.م
• if cannot be put at least make a location should be chosen
• Also could be a bit of 3D given to the logo if it could stay elegent.
Should not have
• Should not show people cleaning.

```html
<!DOCTYPE html>
<html lang="en">
<head>
<meta charset="utf-8">
<title>Brightmoor Facility Care</title>
<link href="https://fonts.googleapis.com/css2?family=Questrial&family=Open+Sans:wght@400;600;700&display=swap" rel="stylesheet">
<style>
:root{
  --lime:#abd036;
  --lime-mid:#9bcb3b;
  --lime-soft:#cadf82;
  --lime-pale:#eaf2ce;
  --forest:#1f8b4f;
  --ink:#2b2b2b;
  --grey:#666;
  --line:#dedede;
  --dark:#1d1d1d;
  --darker:#111;
  --submit:#cbd5a6;
}
*{margin:0;padding:0;box-sizing:border-box}
html,body{width:1200px;height:3191px;overflow:hidden;background:#fff}
body{position:relative;font-family:"Questrial",sans-serif;color:var(--ink)}
.abs{position:absolute}
.photo{position:absolute}

/* header */
.hero{left:0;top:0;width:1200px;height:551px;
  background:
    radial-gradient(ellipse 320px 260px at 680px 230px,rgba(40,150,200,.55),transparent 70%),
    radial-gradient(ellipse 260px 140px at 300px 470px,rgba(255,255,255,.9),transparent 70%),
    linear-gradient(180deg,#5f6770 0%,#8d98a4 20%,#aeb8c2 38%,#6f7782 50%,#4d535c 56%,#cfc9c0 62%,#efece7 80%,#e2ddd5 100%)}
.topbar{left:0;top:0;width:1200px;height:110px;background:rgba(20,20,20,.9)}
.brand{left:86px;top:26px;display:flex;align-items:center;gap:12px}
.brand-dot{width:36px;height:36px;border-radius:50%;background:var(--lime-mid)}
.brand-name{color:#fff;font-size:19px}
.phone-top{left:842px;top:47px;color:#fff;font-size:16px;display:flex;align-items:center;gap:8px}
.search{left:1000px;top:45px;width:112px;height:22px;border:1px solid #ccc;border-radius:11px;color:#ccc;font-size:10px;padding:4px 12px}
.nav{left:676px;top:83px;display:flex;color:#fff;font-size:15px}
.nav span{padding:0 30px;border-left:1px solid #fff;line-height:16px}
.nav span:first-child{border-left:none}
.nav span:last-child{padding-right:0}
.slide-arrow{top:262px;width:40px;height:40px;border-radius:50%;background:rgba(255,255,255,.35)}

.infobar{left:0;top:551px;width:1200px;height:79px;background:var(--forest);display:flex}
.info{flex:1;display:flex;align-items:center;padding:0 60px 0 86px;color:#fff;position:relative;border-left:1px solid rgba(255,255,255,.3)}
.info:first-child{border-left:none}
.info svg{margin-right:26px}
.info h4{font-family:"Open Sans",sans-serif;font-weight:700;font-size:14px;margin-bottom:8px}
.info p{font-size:13px}
.info .go{position:absolute;right:26px;top:29px;width:22px;height:22px;border-radius:50%;background:var(--lime)}

/* section headings */
.heading{left:0;width:1200px;text-align:center;font-size:37px;color:#333;display:flex;justify-content:center;align-items:center;gap:10px}
.heading .rule{width:40px;height:2px;background:#333}

/* services */
.svc-item{left:85px;width:326px;height:102px;border:1px solid var(--line);display:flex;align-items:center;padding-left:20px}
.svc-item.active{background:var(--lime-pale);border-color:var(--lime-soft)}
.svc-item h5{font-size:15px;font-weight:400;color:#333;margin-bottom:6px}
.svc-item .bar{width:48px;height:1px;background:#999;margin-bottom:7px}
.svc-item p{font-size:10px;color:#555;line-height:14px;width:210px}
.svc-item svg{margin-right:24px;flex:none}
.card{top:734px;width:326px;height:336px;border:1px solid var(--line)}
.card .photo{left:0;top:10px;width:324px;height:191px}
.card h5{position:absolute;left:26px;top:222px;font-size:15px;font-weight:400}
.card .bar{position:absolute;left:26px;top:246px;width:48px;height:1px;background:#999}
.card p{position:absolute;left:26px;top:256px;width:280px;font-size:11px;line-height:16px;color:#555}
.card .btn{position:absolute;left:26px;top:303px;padding:5px 16px;background:var(--lime-pale);border:1px solid var(--lime-soft);font-size:10px;color:#444}

/* band */
.band{left:0;top:1130px;width:1200px;height:166px;
  background:
    radial-gradient(ellipse 260px 160px at 520px 80px,rgba(230,240,160,.45),transparent 70%),
    linear-gradient(90deg,var(--lime-mid),var(--lime) 45%,#b8d64a 70%,var(--lime-mid))}
.band h3{position:absolute;left:88px;top:44px;font-size:22px;font-weight:400;color:#2a3a10;display:flex;align-items:center;gap:12px}
.band h3 .rule{width:46px;height:2px;background:#2a3a10}
.band p{position:absolute;left:88px;top:88px;width:520px;font-size:15px;line-height:27px;color:#2d3d12}
.join{left:823px;top:1182px;width:260px;height:64px;border:2px solid #2a3a10;font-size:27px;color:#2a3a10;display:flex;align-items:center;justify-content:center}

/* booking */
.booking-bg{left:0;top:1873px;width:1200px;height:442px;
  background:
    radial-gradient(ellipse 200px 160px at 120px 140px,rgba(220,40,70,.55),transparent 70%),
    radial-gradient(ellipse 220px 180px at 260px 330px,rgba(150,200,90,.7),transparent 70%),
    radial-gradient(ellipse 180px 140px at 90px 40px,rgba(40,110,200,.6),transparent 70%),
    linear-gradient(90deg,#5e8ec8 0%,#a9c3e0 32%,#f3f5f8 52%,#e6ebf2 100%)}
.booking{left:575px;top:1911px;width:534px;height:370px;background:var(--lime-pale);border:2px solid #f4f8e6}
.booking h3{position:absolute;left:0;top:28px;width:100%;text-align:center;font-size:27px;font-weight:400;display:flex;justify-content:center;align-items:center;gap:10px}
.booking h3 .rule{width:40px;height:2px;background:#333}
.field{position:absolute;height:38px;background:#fff;font-size:11px;color:#aaa;padding:12px 14px}
.submit{position:absolute;left:69px;top:304px;width:396px;height:40px;background:var(--submit);text-align:center;font-size:14px;color:#555;line-height:40px}

/* blog */
.post{top:2496px;width:326px}
.post .photo{position:static;width:326px;height:209px}
.post h5{margin-top:22px;font-size:17px;font-weight:400;color:#222}
.post .bar{width:48px;height:1px;background:#999;margin:8px 0}
.post p{font-size:11px;line-height:18px;color:#555}
.post .meta{margin-top:16px;font-size:11px;color:#777;font-style:italic;display:flex;gap:20px}

/* footer */
.footer{left:0;top:2900px;width:1200px;height:245px;background:var(--dark)}
.footer h6{position:absolute;font-family:"Open Sans",sans-serif;font-weight:600;font-size:13px;color:#fff}
.footer .about{position:absolute;left:112px;top:110px;width:220px;font-size:10px;line-height:14px;color:#ddd}
.footer ul{position:absolute;list-style:none;color:#fff;font-size:13px}
.footer li{margin-bottom:11px}
.footer li::before{content:"→";margin-right:14px}
.footer .vline{position:absolute;top:60px;width:1px;height:150px;background:#3a3a3a}
.news-in{position:absolute;left:876px;top:111px;width:188px;height:36px;background:#e5e5e5;font-size:10px;color:#888;padding:12px 10px}
.news-btn{position:absolute;left:1064px;top:111px;width:40px;height:36px;background:var(--lime);display:flex;align-items:center;justify-content:center}
.copy{left:0;top:3145px;width:1200px;height:46px;background:var(--darker);color:#ccc;font-size:11px;text-align:center;line-height:46px}
</style>
</head>
<body>

<!-- Header -->
<div class="abs hero photo" role="img" aria-label="Bright office lounge with tall windows overlooking a waterfront city skyline at dusk"></div>
<div class="abs topbar"></div>
<div class="abs brand"><span class="brand-dot"></span><span class="brand-name">Brightmoor Facility Care</span></div>
<div class="abs phone-top">
  <svg width="16" height="16" viewBox="0 0 16 16"><circle cx="8" cy="8" r="8" fill="#fff"/><path d="M5 4l2 2-1 1c.6 1.3 1.7 2.4 3 3l1-1 2 2-1.5 1.5C7 12 4 9 3.5 5.5z" fill="#1d1d1d"/></svg>
  (555) 318-2046
</div>
<div class="abs search">Search...</div>
<nav class="abs nav"><span>Home</span><span>About Us</span><span>Services</span><span>Contact Us</span></nav>
<div class="abs slide-arrow" style="left:24px"></div>
<div class="abs slide-arrow" style="left:1140px"></div>

<div class="abs infobar">
  <div class="info">
    <svg width="44" height="44" viewBox="0 0 44 44" fill="none" stroke="#fff" stroke-width="2.5"><circle cx="22" cy="22" r="19"/><path d="M22 10v12l8 5"/></svg>
    <div><h4>Opening Hours</h4><p>Mon-Fri: 8:00 AM – 9:00 PM</p></div><span class="go"></span>
  </div>
  <div class="info">
    <svg width="44" height="44" viewBox="0 0 44 44" fill="none" stroke="#fff" stroke-width="2.5"><path d="M4 22L22 6l18 16M9 18v20h26V18M18 38V26h8v12"/></svg>
    <div><h4>Address</h4><p>12 Harbor Lane, Riffa</p></div><span class="go"></span>
  </div>
  <div class="info">
    <svg width="44" height="44" viewBox="0 0 44 44" fill="none" stroke="#fff" stroke-width="2.5"><rect x="12" y="3" width="20" height="38" rx="3"/><path d="M12 9h20M12 33h20"/></svg>
    <div><h4>Phone</h4><p>0800 41 7720</p></div><span class="go"></span>
  </div>
</div>

<!-- What we do -->
<div class="abs heading" style="top:676px">
  <svg width="26" height="16" viewBox="0 0 26 16"><path d="M1 14C6 0 20 0 25 2 22 12 10 17 1 14z" fill="var(--lime-mid)"/></svg>What We Do<span class="rule"></span>
</div>

<div class="abs svc-item active" style="top:745px">
  <svg width="36" height="44" viewBox="0 0 36 44" fill="none" stroke="var(--forest)" stroke-width="2"><path d="M8 4v30M4 34h10l2 8H2z"/><rect x="20" y="22" width="12" height="16"/><path d="M22 22v-5h8v5"/></svg>
  <div><h5>GENERAL CLEANING</h5><div class="bar"></div><p>When you starting a company you are thinking on how to cut expenses</p></div>
</div>
<div class="abs svc-item" style="top:864px">
  <svg width="36" height="44" viewBox="0 0 36 44" fill="none" stroke="var(--forest)" stroke-width="2"><circle cx="14" cy="10" r="6"/><path d="M4 40V28c0-6 4-9 10-9s10 3 10 9v12"/><rect x="22" y="30" width="10" height="10"/></svg>
  <div><h5>COMMERCIALS CLEANING</h5><div class="bar"></div><p>When you starting a company you are thinking on how to cut expenses</p></div>
</div>
<div class="abs svc-item" style="top:981px">
  <svg width="36" height="44" viewBox="0 0 36 44" fill="none" stroke="var(--forest)" stroke-width="2"><path d="M18 2v26M10 28h16l4 14H6zM12 34l-2 8M18 34v8M24 34l2 8"/></svg>
  <div><h5>MAINTANCES SERVICES</h5><div class="bar"></div><p>When you starting a company you are thinking on how to cut expenses</p></div>
</div>

<div class="abs card" style="left:436px">
  <div class="photo" role="img" aria-label="Gloved hand wiping a polished wooden surface" style="background:radial-gradient(ellipse 90px 70px at 180px 70px,rgba(255,255,255,.75),transparent 70%),linear-gradient(160deg,#4f93c9 0%,#7db4df 45%,#c58a4f 70%,#9b5f2c 100%)"></div>
  <h5>GREEN CLEAN SERVICES</h5><div class="bar"></div>
  <p>When you starting a company you are thinking on how to cut expenses.</p>
  <span class="btn">Learn More</span>
</div>
<div class="abs card" style="left:787px">
  <div class="photo" role="img" aria-label="Window cleaners working on a glass building facade" style="background:radial-gradient(ellipse 120px 80px at 120px 100px,rgba(150,200,240,.6),transparent 70%),linear-gradient(135deg,#2a65a8,#5f9bd3 50%,#2f6cb2)"></div>
  <h5>APARTMENT CLEANING</h5><div class="bar"></div>
  <p>When you starting a company you are thinking on how to cut expenses.</p>
  <span class="btn">Learn More</span>
</div>

<!-- Band -->
<div class="abs band">
  <h3><svg width="26" height="16" viewBox="0 0 26 16"><path d="M1 14C6 0 20 0 25 2 22 12 10 17 1 14z" fill="#2a3a10"/></svg>CLEANING SERVICES<span class="rule"></span></h3>
  <p>There are many variations of passages of Lorem Ipsum available, but the majority have suffered alteration in some form</p>
</div>
<div class="abs join">Join Us Now</div>

<!-- Our works -->
<div class="abs heading" style="top:1378px">
  <svg width="26" height="16" viewBox="0 0 26 16"><path d="M1 14C6 0 20 0 25 2 22 12 10 17 1 14z" fill="var(--lime-mid)"/></svg>Our Works<span class="rule"></span>
</div>
<div class="photo" role="img" aria-label="Pink spray bottle and blue glove over a counter" style="left:85px;top:1458px;width:326px;height:347px;background:radial-gradient(ellipse 90px 80px at 110px 110px,rgba(230,70,150,.55),transparent 70%),radial-gradient(ellipse 80px 70px at 300px 240px,rgba(90,150,210,.55),transparent 70%),linear-gradient(135deg,#f4f4f6,#cfd3dc 55%,#eef0f3)"></div>
<div class="photo" role="img" aria-label="Gloved hands with spray bottle and cloth at a window" style="left:436px;top:1458px;width:326px;height:159px;background:radial-gradient(ellipse 70px 60px at 110px 90px,rgba(220,40,60,.5),transparent 70%),linear-gradient(120deg,#d6dbd0,#5eab4e 50%,#e7d248)"></div>
<div class="photo" role="img" aria-label="Vacuum cleaner on a bright tiled floor" style="left:787px;top:1458px;width:326px;height:159px;background:radial-gradient(ellipse 60px 40px at 150px 110px,rgba(40,50,80,.45),transparent 70%),linear-gradient(180deg,#f1efeb,#d2cdc4 60%,#ebe8e2)"></div>
<div class="photo" role="img" aria-label="Spray bottle and sponge in green gloves against blue sky" style="left:436px;top:1645px;width:326px;height:160px;background:radial-gradient(ellipse 70px 60px at 80px 70px,rgba(230,60,160,.5),transparent 70%),radial-gradient(ellipse 80px 70px at 250px 100px,rgba(110,190,60,.75),transparent 70%),linear-gradient(135deg,#5ea8dc,#a8d4f0)"></div>
<div class="photo" role="img" aria-label="Mop and green bucket on a wooden floor" style="left:787px;top:1645px;width:326px;height:160px;background:radial-gradient(ellipse 70px 60px at 260px 70px,rgba(190,220,60,.85),transparent 70%),linear-gradient(160deg,#efe8dc 0%,#d8a46a 35%,#c07e44 100%)"></div>

<!-- Booking -->
<div class="abs booking-bg photo" role="img" aria-label="Blue bucket of cleaning supplies with gloves, brushes and spray bottles"></div>
<div class="abs booking">
  <h3><svg width="26" height="16" viewBox="0 0 26 16"><path d="M1 14C6 0 20 0 25 2 22 12 10 17 1 14z" fill="var(--lime-mid)"/></svg>Service Booking<span class="rule"></span></h3>
  <div class="field" style="left:69px;top:81px;width:179px">Name.....</div>
  <div class="field" style="left:285px;top:81px;width:180px">Phone.....</div>
  <div class="field" style="left:69px;top:141px;width:179px">Email.....</div>
  <div class="field" style="left:285px;top:141px;width:180px">Date.....</div>
  <div class="field" style="left:69px;top:203px;width:396px;height:80px">Message.....</div>
  <div class="submit">Submit</div>
</div>

<!-- Blog -->
<div class="abs heading" style="top:2417px">
  <svg width="26" height="16" viewBox="0 0 26 16"><path d="M1 14C6 0 20 0 25 2 22 12 10 17 1 14z" fill="var(--lime-mid)"/></svg>Recent Blog<span class="rule"></span>
</div>
<article class="abs post" style="left:85px">
  <div class="photo" role="img" aria-label="Freshly wiped white counter in a bright room" style="background:radial-gradient(ellipse 90px 70px at 220px 80px,rgba(40,170,200,.45),transparent 70%),linear-gradient(180deg,#c9a57c 0%,#e6d8c6 45%,#f5f5f5 70%,#e9e9e9)"></div>
  <h5>LOREM IPSUM DOLOR</h5><div class="bar"></div>
  <p>It is a long established fact that a reader will be distracted by the readable content of a page when looking at its layout.</p>
  <div class="meta"><span>◷ 23rd may 2016</span><span>▢ 0 comments</span></div>
</article>
<article class="abs post" style="left:436px">
  <div class="photo" role="img" aria-label="Yellow sponge polishing a chrome tap" style="background:radial-gradient(ellipse 90px 60px at 200px 90px,rgba(40,160,200,.55),transparent 70%),radial-gradient(ellipse 90px 50px at 140px 160px,rgba(240,210,50,.8),transparent 70%),linear-gradient(135deg,#eef1f4,#c5d3de)"></div>
  <h5>LOREM IPSUM DOLOR</h5><div class="bar"></div>
  <p>It is a long established fact that a reader will be distracted by the readable content of a page when looking at its layout.</p>
  <div class="meta"><span>◷ 23rd may 2016</span><span>▢ 0 comments</span></div>
</article>
<article class="abs post" style="left:787px">
  <div class="photo" role="img" aria-label="Bucket full of colourful cleaning products" style="background:radial-gradient(ellipse 80px 60px at 160px 90px,rgba(230,60,150,.5),transparent 70%),radial-gradient(ellipse 90px 60px at 150px 180px,rgba(240,210,50,.8),transparent 70%),linear-gradient(135deg,#8cc43c,#56a8d8 60%,#7cbf3e)"></div>
  <h5>LOREM IPSUM DOLOR</h5><div class="bar"></div>
  <p>It is a long established fact that a reader will be distracted by the readable content of a page when looking at its layout.</p>
  <div class="meta"><span>◷ 23rd may 2016</span><span>▢ 0 comments</span></div>
</article>

<!-- Footer -->
<footer class="abs footer">
  <h6 style="left:112px;top:72px">About Us</h6>
  <p class="about">Totam rem aperiam, eaque ipsa quae ab illo inventore veritatis et quasi architecto beatae vitae dicta sunt explicabo. Nemo enim ipsam voluptatem quia voluptas sit</p>
  <div class="vline" style="left:354px"></div>
  <h6 style="left:418px;top:63px">Quick Links</h6>
  <ul style="left:410px;top:106px"><li>Home</li><li>About us</li><li>Services</li><li>Contact us</li></ul>
  <div class="vline" style="left:576px"></div>
  <h6 style="left:635px;top:63px">Services</h6>
  <ul style="left:635px;top:106px"><li style="margin-bottom:18px">general cleaning</li><li style="margin-bottom:18px">commercials cleaning</li><li>maintances services</li></ul>
  <div class="vline" style="left:826px"></div>
  <h6 style="left:876px;top:67px">Subscribe Newsletter</h6>
  <div class="news-in">Enter Your Email ID.....</div>
  <div class="news-btn"><svg width="18" height="13" viewBox="0 0 18 13" fill="none" stroke="#fff" stroke-width="1.6"><rect x="1" y="1" width="16" height="11"/><path d="M1 1l8 6 8-6"/></svg></div>
</footer>
<div class="abs copy">brightmoorcare.com 2017. All rights reserved</div>

</body>
</html>
```